依頼詳細
サイズ:[長形3号]・[角形2号]
でお願いします。

注1:ロゴデータは、アルファベット『RIKUMAI』がメインです。
漢字のパターンも一応添付させて頂きますので、必要であればお使いください。
記載項目
【封筒】

社名:株式会社 陸舞
(英字表記:RIKUMAI)

住所:〒111-1111
大阪市××××××××××××××

TEL:00-0000-0000
FAX:00-0000-0000

以上になります。
半角・全角・ハイフン有無等は、調整して頂いて結構です。
希望イメージ
シンプル 複雑
単色 カラフル
暗い 明るい
日常 高級
遊び心 厳粛
未来的 伝統的
女性的 男性的
希望する色
納品ファイル
• 高解像度JPG (.jpg)
• イラストレーター形式 (.ai)
• PNG形式 (.png)
補足説明
■ 選んだ理由

いいデザインに気に入ってます。

■ 提案者全員のお礼・コメント

ありがとうございます。

```html
<!DOCTYPE html>
<html lang="ja">
<head>
<meta charset="utf-8">
<title>株式会社 陸舞 封筒</title>
<link rel="stylesheet" href="https://fonts.googleapis.com/css2?family=Noto+Sans+JP:wght@400;500;700&display=swap">
<style>
  :root {
    --paper: #ffffff;
    --ink: #3b3a45;
    --accent: #d3232c;
    --art-dark: #e4e3e8;
    --art-red: #f6dcdd;
  }
  * { margin: 0; padding: 0; box-sizing: border-box; }
  html, body {
    width: 1200px;
    height: 2600px;
    overflow: hidden;
    background: var(--paper);
  }
  .envelope {
    position: relative;
    width: 1200px;
    height: 2600px;
    background: var(--paper);
    font-family: "Noto Sans JP", sans-serif;
    color: var(--ink);
  }
  .sender {
    position: absolute;
    left: 812px;
    top: 1620px;
    width: 340px;
  }
  .brand-badge {
    width: 64px;
    height: 64px;
    margin: 0 0 34px 128px;
    background: var(--accent);
  }
  .brand-name {
    font-size: 54px;
    font-weight: 500;
    letter-spacing: 5px;
    color: var(--accent);
    line-height: 1;
    white-space: nowrap;
  }
  .company-jp {
    margin-top: 12px;
    margin-left: 92px;
    font-size: 18px;
    font-weight: 500;
    letter-spacing: 2px;
    line-height: 1.3;
    white-space: nowrap;
  }
  .address {
    margin-top: 26px;
    font-size: 17px;
    line-height: 1.6;
    letter-spacing: 1px;
    white-space: nowrap;
  }
  .contact {
    margin-top: 24px;
    font-size: 20px;
    line-height: 1.5;
    letter-spacing: 3px;
    white-space: nowrap;
  }
  .illustration {
    position: absolute;
    left: 72px;
    top: 2090px;
    width: 1056px;
    height: 440px;
    background: linear-gradient(90deg, var(--art-dark) 0%, var(--art-dark) 48%, var(--art-red) 52%, var(--art-red) 100%);
    opacity: 0.7;
  }
</style>
</head>
<body>
  <main class="envelope">
    <section class="sender">
      <div class="brand-badge" aria-hidden="true"></div>
      <div class="brand-name">RIKUMAI</div>
      <div class="company-jp">株式会社 陸舞</div>
      <div class="address">
        <p>〒111-1111</p>
        <p>大阪市 ××××××××××××××</p>
      </div>
      <div class="contact">
        <p>TEL : 00-0000-0000</p>
        <p>FAX : 00-0000-0000</p>
      </div>
    </section>
    <div class="illustration" role="img" aria-label="向かい合って立つ二羽の鳥の線画イラスト（左は濃紺、右は赤）"></div>
  </main>
</body>
</html>
```